Oven Cleaning Business owner needs business card design

Hi there,
Would like for a business card to be designed for myself, the owner of a professional oven cleaning business on the Sunshine Coast.
Would like it to look sleek, and modern-ish. Bit creative is encouraged too.
Include following:
Name/title: Corin ter Haghe, Owner
Phone number: 1300 482 916
Email: info@hearthshinecrew.com.au
Website: www.hearthshinecrew.com.au

```html
<!DOCTYPE html>
<html lang="en">
<head>
<meta charset="utf-8">
<title>Hearthshine Crew – Business Card</title>
<link rel="stylesheet" href="https://fonts.googleapis.com/css2?family=Open+Sans:wdth,wght@75..100,300..800&display=swap">
<style>
  :root {
    --backdrop: #b5b5b5;
    --card-white: #ffffff;
    --teal: #56bfca;
    --ink: #1c1c1e;
    --card-black: #0a0a0c;
    --pattern-tone: #1d1f26;
  }
  * { margin: 0; padding: 0; box-sizing: border-box; }
  html, body {
    width: 1200px;
    height: 846px;
    overflow: hidden;
    background: var(--backdrop);
    font-family: "Open Sans", Arial, sans-serif;
  }
  .stage { position: relative; width: 1200px; height: 846px; }

  .card {
    position: absolute;
    width: 520px;
    height: 318px;
    border-radius: 30px;
    overflow: hidden;
  }

  /* Front side */
  .card-front { left: 60px; top: 110px; background: var(--card-white); }
  .front-shape { position: absolute; inset: 0; }
  .brand-name {
    position: absolute;
    left: 150px;
    top: 168px;
    width: 116px;
    text-align: center;
    font-stretch: 75%;
    font-weight: 800;
    font-size: 18px;
    line-height: 1.05;
    text-transform: uppercase;
    letter-spacing: 0.5px;
    color: var(--ink);
  }
  .contact {
    position: absolute;
    left: 286px;
    top: 112px;
    font-stretch: 75%;
    color: var(--ink);
  }
  .contact-name {
    font-size: 20px;
    font-weight: 700;
    color: var(--teal);
    letter-spacing: -0.2px;
  }
  .contact-title {
    font-size: 11px;
    font-weight: 400;
    color: var(--ink);
    margin-left: 4px;
  }
  .contact-line {
    font-size: 15px;
    font-weight: 300;
    line-height: 1.4;
  }
  .contact-list { list-style: none; margin-top: 4px; }

  /* Back side */
  .card-back { left: 620px; top: 418px; background: var(--card-black); }
  .back-pattern {
    position: absolute;
    inset: 0;
    background: linear-gradient(135deg, var(--card-black) 0%, var(--pattern-tone) 50%, var(--card-black) 100%);
    opacity: 0.55;
  }
  .back-brand {
    position: absolute;
    inset: 0;
    display: flex;
    align-items: center;
    justify-content: center;
    font-stretch: 75%;
    font-weight: 800;
    font-size: 28px;
    letter-spacing: 1.5px;
    text-transform: uppercase;
    color: var(--teal);
  }
</style>
</head>
<body>
<main class="stage">

  <section class="card card-front" aria-label="Business card front">
    <svg class="front-shape" viewBox="0 0 520 318" width="520" height="318" aria-hidden="true">
      <rect class="teal-field" x="0" y="0" width="520" height="318" fill="var(--teal)"/>
      <ellipse class="arc-line" cx="420" cy="58" rx="328" ry="308" fill="none" stroke="var(--card-white)" stroke-width="2"/>
      <ellipse class="white-field" cx="420" cy="58" rx="320" ry="300" fill="var(--card-white)"/>
      <ellipse class="arc-line-inner" cx="420" cy="58" rx="314" ry="294" fill="none" stroke="var(--teal)" stroke-width="1.6"/>
    </svg>

    <div class="brand-name">Hearthshine<br>Crew</div>

    <div class="contact">
      <p><span class="contact-name">Corin ter Haghe</span><span class="contact-title">Owner</span></p>
      <ul class="contact-list">
        <li class="contact-line">Phone number: 1300 482 916</li>
        <li class="contact-line">info@hearthshinecrew.com.au</li>
        <li class="contact-line">www.hearthshinecrew.com.au</li>
      </ul>
    </div>
  </section>

  <section class="card card-back" aria-label="Business card back">
    <div class="back-pattern" role="img" aria-label="Faint repeated brand name pattern on black"></div>
    <div class="back-brand">Hearthshine Crew</div>
  </section>

</main>
</body>
</html>
```